Cleaning Company and Staynest Tasks

Our London based company provides services for all things related to Staynest. Our main tasks are cleaning, checkins & linen. We are in need of a fresh new design that allows customers to book our services with ease.

The site must keep in mind that it will be primarily used on mobile and payment to be taken online.

What we require:

- Two pages designed, Home page (see Homepage doc) and Purchase Page (see flow chart)

Things we like:-

- We like mainly white and pastel based colours.
- Usage of vector style graphics through our the site to represent people & tasks.
- Shopping cart, with lots of images to select services
- Shopping cart that always has the pricing floating on the right
- Shopping cart that is wizard based.
- We like the usage of wonk characters on this site (for us probably angels)
http://www.tradelarks.com/pricing.php
- Slightly quirky design.

Sites we like:
http://vantageforge.com/ - bold action
https://www.mailorbit.com/ - a very playful design

TO AVOID WASTING TIME, INITIALLY DESIGN THE FRONT PAGE ONLY, IF WE LIKE YOUR HOME PAGE DESIGN THEM WE CAN SHORT LIST YOU INTO DESIGNING THE PAYMENT WIZARD PAGE

Target Market(s)

Young working professionals.

Industry/Entity Type

Cleaning Service

Contact Information for Business Card

Name: Rob Patel
Title: Senior Sales Representative
Tel: +44 (0) 777 4818 5096
Office: +44 (0) 207 413 6871
email: mh@fernhollowstays.co.uk
web: www.fernhollowstays.co.uk

Number of Pages Required

2 page

Font styles to use
Sans Serif

Colors
876aae
6b449b

Requirements
Must have
• - Two pages designed including home page and wizard to purchase services.
• - Usage of vector images.
Nice to have
• Angels to represent tasks
• We also like the colour yellow, the branding can be changed to suit this colour change.
Should not have
• A design that must not look like a Pagecraft standard Pagecraft theme.

```html
<!DOCTYPE html>
<html lang="en">
<head>
<meta charset="utf-8">
<title>fernhollowstays – Book a local professional cleaner</title>
<link href="https://fonts.googleapis.com/css2?family=Roboto:wght@300;400;500;700&display=swap" rel="stylesheet">
<style>
:root{
  --purple:#6b449b;
  --lilac:#876aae;
  --lilac-soft:#9a82bf;
  --ink:#3a3a3a;
  --muted:#8a8a8a;
  --line:#e4e4e4;
  --white:#ffffff;
  --pale:#f4f3f6;
  --footer:#f7f7f7;
}
*{margin:0;padding:0;box-sizing:border-box}
html,body{width:1200px;height:2736px;overflow:hidden}
body{font-family:'Roboto',Arial,sans-serif;color:var(--ink);background:var(--white)}
.page{position:relative;width:1200px;height:2736px}

/* hero */
.hero{position:relative;height:640px;overflow:hidden}
.hero-photo{position:absolute;inset:0;background:linear-gradient(180deg,#5d5872 0%,#4a4760 40%,#2e2a3a 75%,#3c3244 100%)}
.hero-tint{position:absolute;inset:0;background:linear-gradient(180deg,rgba(107,68,155,.35),rgba(40,30,60,.35))}
.topbar{position:absolute;top:0;left:0;right:0;height:64px;background:rgba(60,40,90,.55);display:flex;align-items:center;padding:0 36px}
.brand{display:flex;align-items:center;gap:10px;color:var(--white);font-size:26px;font-weight:300}
.brand-mark{width:24px;height:24px;border-radius:50%;background:var(--white)}
.nav{margin-left:auto;display:flex;align-items:center;gap:44px;font-size:14px;color:var(--white);letter-spacing:.5px}
.nav .login{border:1px solid var(--white);border-radius:16px;padding:6px 18px}
.hero-copy{position:absolute;top:200px;left:0;right:0;text-align:center;color:var(--white)}
.hero-title{font-size:40px;font-weight:400;letter-spacing:1px}
.hero-btn{display:inline-block;margin-top:28px;border:2px solid var(--white);border-radius:22px;padding:10px 26px;font-size:14px;letter-spacing:1px}
.hero-arrows{position:absolute;right:40px;bottom:60px;display:flex;gap:10px}
.hero-arrows span{width:30px;height:30px;border:1px solid rgba(255,255,255,.7);border-radius:50%;display:flex;align-items:center;justify-content:center}

/* section titles */
.section-title{text-align:center;font-size:34px;font-weight:300;letter-spacing:1px}
.section-rule{width:60px;height:2px;background:var(--lilac);margin:14px auto 0}

/* services */
.services{height:460px;padding-top:60px}
.service-grid{display:grid;grid-template-columns:1fr 1fr;gap:56px 80px;width:900px;margin:60px auto 0}
.service{display:flex;gap:22px}
.service-icon{flex:0 0 64px;height:64px;border:2px solid var(--line);border-radius:50%;display:flex;align-items:center;justify-content:center}
.service h3{font-size:16px;font-weight:500;letter-spacing:.5px;margin:6px 0 8px}
.service p{font-size:12px;line-height:1.6;color:var(--muted)}

/* why us */
.why{height:500px;background:var(--lilac);color:var(--white);padding-top:60px}
.why .section-rule{background:var(--white)}
.why-grid{display:grid;grid-template-columns:repeat(3,260px);gap:28px;justify-content:center;margin-top:40px}
.why-photo{height:200px;border:4px solid var(--white)}
.why-photo.a{background:linear-gradient(135deg,#e9e6ef,#c9c1d4)}
.why-photo.b{background:linear-gradient(135deg,#c7dbe2,#8fb1bf)}
.why-photo.c{background:linear-gradient(135deg,#d9d2c9,#a5c1d2)}
.why h3{font-size:20px;font-weight:400;margin:14px 0 8px}
.why p{font-size:12px;line-height:1.5;opacity:.9}
.why .more{font-size:12px;margin-top:8px;display:block}

/* how */
.how{height:400px;padding-top:70px}
.steps{display:grid;grid-template-columns:repeat(4,200px);gap:40px;justify-content:center;margin-top:54px;text-align:center}
.step-icon{width:100px;height:100px;border-radius:50%;background:var(--pale);border:1px solid var(--line);margin:0 auto;display:flex;align-items:center;justify-content:center}
.step p{font-size:14px;line-height:1.45;margin-top:22px}

/* testimonials */
.testimonials{height:380px;background:var(--pale);text-align:center;padding-top:30px}
.testimonials .section-title{color:var(--lilac)}
.testimonials .lead{font-size:14px;color:var(--muted);margin-top:10px}
.quote-row{display:flex;align-items:center;justify-content:center;gap:60px;margin-top:20px}
.quote-row .arrow{font-size:28px;color:var(--muted)}
.avatar{width:90px;height:90px;border-radius:50%;background:linear-gradient(160deg,#cbbfae,#7b6d62);border:3px solid var(--white)}
.quote{width:920px;margin:26px auto 0;font-size:13px;line-height:1.7;color:var(--muted)}
.quote-name{margin-top:20px;font-size:14px;color:var(--lilac)}

/* footer */
.footer{height:356px;background:var(--white);border-top:1px solid var(--line)}
.footer-cols{display:grid;grid-template-columns:300px 230px 290px 200px;gap:30px;width:1100px;margin:0 auto;padding-top:40px}
.footer h4{font-size:13px;font-weight:500;letter-spacing:.5px;margin-bottom:16px}
.footer p,.footer li{font-size:12px;line-height:1.75;color:var(--muted);list-style:none}
.footer li::before{content:"› ";color:var(--lilac)}
.signup{display:flex;margin-top:10px}
.signup span{flex:1;border:1px solid var(--line);padding:7px 10px;font-size:12px;color:var(--muted)}
.signup b{background:var(--purple);color:var(--white);font-size:12px;font-weight:400;padding:7px 12px}
.social{display:flex;gap:10px}
.social span{width:26px;height:26px;background:var(--ink);border-radius:3px}
.copyright{position:absolute;left:0;right:0;bottom:0;height:50px;border-top:1px solid var(--line);text-align:center;font-size:12px;line-height:50px;color:var(--muted)}
</style>
</head>
<body>
<div class="page">

<header class="hero">
  <div class="hero-photo" role="img" aria-label="Evening photograph of the London city skyline with office towers"></div>
  <div class="hero-tint"></div>
  <div class="topbar">
    <div class="brand"><span class="brand-mark"></span>fernhollowstays</div>
    <nav class="nav"><span>HOME</span><span>ABOUT</span><span>CONTACT</span><span class="login">LOGIN</span></nav>
  </div>
  <div class="hero-copy">
    <h1 class="hero-title">BOOK A LOCAL PROFESSIONAL CLEANER</h1>
    <span class="hero-btn">BOOK A SERVICE</span>
  </div>
  <div class="hero-arrows">
    <span><svg width="10" height="14" viewBox="0 0 10 14"><path d="M8 1 2 7l6 6" stroke="#fff" stroke-width="2" fill="none"/></svg></span>
    <span><svg width="10" height="14" viewBox="0 0 10 14"><path d="m2 1 6 6-6 6" stroke="#fff" stroke-width="2" fill="none"/></svg></span>
  </div>
</header>

<section class="services">
  <h2 class="section-title">WHAT WE DO</h2>
  <div class="section-rule"></div>
  <div class="service-grid">
    <div class="service">
      <div class="service-icon"><svg width="30" height="24" viewBox="0 0 30 24" fill="#6b449b"><circle cx="9" cy="6" r="5"/><circle cx="21" cy="6" r="5"/><path d="M0 24c0-7 4-10 9-10s9 3 9 10zM14 24c1-6 3-10 7-10 5 0 9 3 9 10z"/></svg></div>
      <div><h3>STAYNEST TASKS</h3><p>Lorem Ipsum has been the industry's standard dummy text ever since the 1500s, when an unknown printer took a galley of type and scrambled it to make a specimen book.</p></div>
    </div>
    <div class="service">
      <div class="service-icon"><svg width="30" height="24" viewBox="0 0 30 24"><rect x="1" y="1" width="28" height="17" rx="2" stroke="#6b449b" stroke-width="2" fill="none"/><path d="M10 23h10M15 18v5" stroke="#6b449b" stroke-width="2"/></svg></div>
      <div><h3>STAYNEST MANAGEMENT</h3><p>Lorem Ipsum has been the industry's standard dummy text ever since the 1500s, when an unknown printer took a galley of type and scrambled it to make a specimen book.</p></div>
    </div>
    <div class="service">
      <div class="service-icon"><svg width="26" height="26" viewBox="0 0 26 26"><circle cx="13" cy="13" r="11" stroke="#6b449b" stroke-width="2" fill="none"/><path d="M13 6v14M6 13h14" stroke="#6b449b" stroke-width="2"/></svg></div>
      <div><h3>DOMESTIC CLEANING</h3><p>Lorem Ipsum has been the industry's standard dummy text ever since the 1500s, when an unknown printer took a galley of type and scrambled it to make a specimen book.</p></div>
    </div>
    <div class="service">
      <div class="service-icon"><svg width="30" height="24" viewBox="0 0 30 24"><rect x="1" y="1" width="28" height="17" rx="2" stroke="#6b449b" stroke-width="2" fill="none"/><path d="M10 23h10M15 18v5" stroke="#6b449b" stroke-width="2"/></svg></div>
      <div><h3>HANDYMAN</h3><p>Lorem Ipsum has been the industry's standard dummy text ever since the 1500s, when an unknown printer took a galley of type and scrambled it to make a specimen book.</p></div>
    </div>
  </div>
</section>

<section class="why">
  <h2 class="section-title">WHY US</h2>
  <div class="section-rule"></div>
  <div class="why-grid">
    <article>
      <div class="why-photo a" role="img" aria-label="Photograph of a cleaner tidying a bright living room"></div>
      <h3>Trusted Professionals</h3>
      <p>Our team is vetted and trained to the highest standard. Every cleaner is checked, insured and rated by guests.</p>
      <span class="more">Read More »</span>
    </article>
    <article>
      <div class="why-photo b" role="img" aria-label="Photograph of a cleaner wiping a glass surface"></div>
      <h3>Same day Availability</h3>
      <p>Book before 11am for same day cleaning, and schedule your stay turnovers as early as the same day.</p>
      <span class="more">Read More »</span>
    </article>
    <article>
      <div class="why-photo c" role="img" aria-label="Photograph of a smiling cleaner polishing a table"></div>
      <h3>Our Guarantee</h3>
      <p>If you are not satisfied with our work, we'll send a cleaner back to do it again for free.</p>
      <span class="more">Read More »</span>
    </article>
  </div>
</section>

<section class="how">
  <h2 class="section-title">HOW IT WORKS</h2>
  <div class="section-rule"></div>
  <div class="steps">
    <div class="step">
      <div class="step-icon"><svg width="36" height="36" viewBox="0 0 36 36"><circle cx="18" cy="18" r="15" stroke="#6b449b" stroke-width="2.5" fill="none"/><path d="m11 18 5 5 9-10" stroke="#6b449b" stroke-width="2.5" fill="none"/></svg></div>
      <p>Select a service</p>
    </div>
    <div class="step">
      <div class="step-icon"><svg width="36" height="36" viewBox="0 0 36 36"><circle cx="18" cy="18" r="15" stroke="#6b449b" stroke-width="2.5" fill="none"/><path d="M18 9v9l6 4" stroke="#6b449b" stroke-width="2.5" fill="none"/></svg></div>
      <p>Select A time &amp; date you'd like a our professional to attend</p>
    </div>
    <div class="step">
      <div class="step-icon"><svg width="40" height="30" viewBox="0 0 40 30"><rect x="2" y="2" width="36" height="26" rx="3" stroke="#6b449b" stroke-width="2.5" fill="none"/><path d="M2 10h36" stroke="#6b449b" stroke-width="4"/><path d="M8 21h10" stroke="#6b449b" stroke-width="2.5"/></svg></div>
      <p>Pay securely online</p>
    </div>
    <div class="step">
      <div class="step-icon"><svg width="30" height="36" viewBox="0 0 30 36"><path d="M2 2h18l8 8v24H2z" stroke="#6b449b" stroke-width="2.5" fill="none"/><path d="M8 16h14M8 22h14M8 28h10" stroke="#6b449b" stroke-width="2"/></svg></div>
      <p>Sit back, Relax and wait for one of our professionals</p>
    </div>
  </div>
</section>

<section class="testimonials">
  <h2 class="section-title">TESTIMONIALS</h2>
  <p class="lead">Don't just take our word for it; here is what some of our other customers think</p>
  <div class="quote-row">
    <span class="arrow">‹</span>
    <div class="avatar" role="img" aria-label="Round portrait photo of a customer"></div>
    <span class="arrow">›</span>
  </div>
  <p class="quote">“ Lorem Ipsum has been the industry's standard dummy text ever since the 1500s, when an unknown printer took a galley of type and scrambled it to make a type specimen book. It has survived not only five centuries, but also the leap into electronic typesetting, remaining essentially unchanged. It was popularised in the 1960s with the release of Letraset sheets containing passages. ”</p>
  <p class="quote-name">Neque porro quisquam</p>
</section>

<footer class="footer">
  <div class="footer-cols">
    <div>
      <h4>CONTACT US</h4>
      <p>Address : 14 Larkmead Row, London<br>SE1 4QT<br>Phone : +44 (0) 777 4818 5096<br>Office : +44 (0) 207 413 6871<br>Email : mh@fernhollowstays.co.uk</p>
    </div>
    <div>
      <h4>NAVIGATE</h4>
      <ul><li>SERVICES</li><li>ABOUT US</li><li>CAREERS</li><li>FAQS</li><li>CONTACTS</li></ul>
    </div>
    <div>
      <h4>JOIN OUR MAILING LIST</h4>
      <p>Sign up to receive our news and offers</p>
      <div class="signup"><span>Email address</span><b>Submit</b></div>
    </div>
    <div>
      <h4>FOLLOW US OUT THERE</h4>
      <div class="social"><span></span><span></span><span></span><span></span></div>
    </div>
  </div>
  <div class="copyright">Copyright © 2016. All Rights Reserved</div>
</footer>

</div>
</body>
</html>
```